Mobile Fitness snd Therapy Business Card Design

I need a business card designed for my mobile fitness and therapy business.

Please view the images that I have uploaded. I like the simplicity of the design that I have attached. I adapted it with my information

Target Market(s)

Those seeking personal training, injury rehabilitation or massage therapy.

Industry/Entity Type

Business

Contact Information for Business Card

Dylan Marwick - MSc, CAT(C), RMT, CSCS, Pn2
e-mail: dylan@vantrelo.com
website: www.vantrelo.com
instagram: @dylan_marwick

Font styles to use
Sans Serif

Colors
3176b5
0355a3

Requirements
Must have
• "Contact us to receive a FREE assessment"
• Services offered:
• Personal Training
• Golf Fitness
• Injury Rehab
• Massage Therapy
• Yoga
Nice to have
• Consistent colours with brand
• - Dark Blue: #232837
• - Blue: #5096f0
• Consistent look/feel with the website: www.vantrelo.com

```html
<!DOCTYPE html>
<html lang="en">
<head>
<meta charset="utf-8">
<title>Vantrelo Business Card</title>
<link rel="stylesheet" href="https://fonts.googleapis.com/css2?family=Michroma&family=Orbitron:wght@700&family=Montserrat:wght@500;700&display=swap">
<style>
  :root {
    --backdrop: #9a9a9a;
    --card: #ffffff;
    --navy: #232837;
    --blue: #0355a3;
    --blue-mid: #3176b5;
    --blue-light: #5096f0;
    --swoosh: #ececec;
    --light-text: #ffffff;
  }
  * { margin: 0; padding: 0; box-sizing: border-box; }
  html, body { width: 960px; height: 1200px; overflow: hidden; }
  body { background: var(--backdrop); position: relative; }
  .card {
    position: absolute; left: 27px; width: 900px; height: 540px;
    background: var(--card); overflow: hidden;
  }
  .card--front { top: 46px; }
  .card--back { top: 620px; }
  .swoosh-area {
    position: absolute; right: 0; top: 8px; width: 360px; height: 270px;
    background: radial-gradient(ellipse at 80% 40%, var(--swoosh) 0%, rgba(236,236,236,0.5) 45%, rgba(255,255,255,0) 75%);
  }
  .wordmark {
    position: absolute; left: 0; right: 0; text-align: center;
    font-family: "Orbitron", sans-serif; font-weight: 700; color: var(--navy);
    line-height: 1; white-space: nowrap;
  }
  .card--front .wordmark { top: 127px; font-size: 76px; letter-spacing: 2px; }
  .card--back .wordmark { top: 181px; font-size: 106px; letter-spacing: 3px; }
  .tagline {
    position: absolute; left: 0; right: 0; top: 300px; text-align: center;
    font-family: "Montserrat", sans-serif; font-weight: 700; font-size: 34px;
    letter-spacing: 5.2px; color: var(--navy); white-space: nowrap;
  }
  .offer {
    position: absolute; left: 0; right: 0; top: 366px; text-align: center;
    font-family: "Montserrat", sans-serif; font-weight: 700; font-size: 19px;
    letter-spacing: 1.5px; color: var(--blue-mid); white-space: nowrap;
  }
  .band { position: absolute; left: 0; bottom: 0; width: 900px; }
  .card--front .band { height: 228px; }
  .card--back .band { height: 115px; }
  .band svg { display: block; }
  .services {
    position: absolute; left: 90px; top: 28px;
    font-family: "Michroma", sans-serif; font-size: 16px; line-height: 34px;
    color: var(--light-text); list-style: none; letter-spacing: 1px;
  }
  .contact {
    position: absolute; left: 630px; top: 34px; width: 260px;
    font-family: "Montserrat", sans-serif; font-weight: 500; font-size: 14px;
    line-height: 26px; color: var(--light-text); list-style: none;
  }
  .contact .name { font-weight: 700; font-size: 19px; line-height: 28px; }
  .contact .creds { font-size: 12px; color: var(--blue-light); margin-bottom: 8px; }
</style>
</head>
<body>
  <section class="card card--front">
    <div class="swoosh-area" role="img" aria-label="Faint grey curved speed-line decoration"></div>
    <div class="wordmark">VANTRELO</div>
    <div class="band">
      <svg width="900" height="228" viewBox="0 0 900 228">
        <rect width="900" height="228" fill="var(--blue)"/>
        <path d="M900 0 H509 C400 18 345 100 345 228 H900 Z" fill="var(--card)"/>
        <path d="M900 0 H565 C430 0 357 100 357 228 H900 Z" fill="var(--navy)"/>
        <path d="M555 0 H603 V144 A24 24 0 0 1 555 144 Z" fill="var(--blue-mid)"/>
      </svg>
      <ul class="services">
        <li>PERSONAL TRAINING</li>
        <li>GOLF FITNESS</li>
        <li>INJURY REHAB</li>
        <li>MASSAGE THERAPY</li>
        <li>YOGA</li>
      </ul>
      <ul class="contact">
        <li class="name">Dylan Marwick</li>
        <li class="creds">MSc, CAT(C), RMT, CSCS, Pn2</li>
        <li>dylan@vantrelo.com</li>
        <li>www.vantrelo.com</li>
        <li>@dylan_marwick</li>
      </ul>
    </div>
  </section>

  <section class="card card--back">
    <div class="wordmark">VANTRELO</div>
    <div class="tagline">NUTRITION - FITNESS - HEALTH</div>
    <div class="offer">Contact us to receive a FREE assessment</div>
    <div class="band">
      <svg width="900" height="115" viewBox="0 0 900 115">
        <rect width="900" height="115" fill="var(--blue)"/>
        <path d="M900 0 H509 C440 12 395 60 369 115 H900 Z" fill="var(--card)"/>
        <path d="M900 0 H565 C480 0 415 50 383 115 H900 Z" fill="var(--navy)"/>
      </svg>
    </div>
  </section>
</body>
</html>
```